KORVELTA Corporate Business Card

Modern business card design for company which focuses in the areas of Staffing, IT Consulting & Data Services. Please note: We are no longer using the IT subscript on the logo. All designs should have IT subscript removed.
Website: www.korveltait.example

```html
<!DOCTYPE html>
<html lang="en">
<head>
<meta charset="utf-8">
<title>KORVELTA Business Card</title>
<link href="https://fonts.googleapis.com/css2?family=Open+Sans:wght@400;600;700&display=swap" rel="stylesheet">
<style>
  :root {
    --backdrop: #2b2b2b;
    --brand-sky: #219fda;
    --brand-sky-light: #3aaae0;
    --brand-navy: #0b5a96;
    --brand-blue: #1d94d5;
    --paper: #ffffff;
  }
  * { margin: 0; padding: 0; box-sizing: border-box; }
  html, body { width: 1200px; height: 903px; overflow: hidden; }
  body {
    background: var(--backdrop);
    font-family: "Open Sans", Arial, sans-serif;
    position: relative;
  }
  .card {
    position: absolute;
    width: 560px;
    height: 320px;
    border-radius: 18px;
    overflow: hidden;
    box-shadow: 0 12px 30px rgba(0,0,0,0.45);
  }

  /* Front */
  .card-front {
    left: 60px;
    top: 80px;
    background: var(--brand-sky);
  }
  .front-backdrop {
    position: absolute;
    inset: 0;
    background: radial-gradient(ellipse at 50% 45%, var(--brand-sky-light) 0%, var(--brand-sky) 70%);
  }

  .wordmark {
    position: absolute;
    display: flex;
    align-items: center;
    gap: 12px;
    font-weight: 700;
    letter-spacing: 2px;
    line-height: 1;
    white-space: nowrap;
  }
  .wordmark-mark { width: 30px; height: 30px; flex: none; }
  .front-wordmark {
    left: 50%;
    top: 118px;
    transform: translateX(-50%);
    color: var(--paper);
    font-size: 64px;
  }
  .front-wordmark .wordmark-mark { border: 4px solid var(--paper); border-radius: 4px; }

  .tagline {
    position: absolute;
    left: 0; right: 0;
    bottom: 42px;
    text-align: center;
    color: var(--paper);
    font-size: 15px;
  }
  .tagline .dot {
    display: inline-block;
    width: 5px; height: 5px;
    background: var(--paper);
    margin: 0 6px 2px;
  }

  /* Back */
  .card-back {
    left: 580px;
    top: 480px;
    background: var(--paper);
  }
  .back-band {
    position: absolute;
    left: 0; right: 0; bottom: 0;
    height: 150px;
    background: var(--brand-navy);
  }
  .back-frame {
    position: absolute;
    inset: 10px;
    border: 2px solid var(--brand-navy);
    border-radius: 12px;
  }
  .back-wordmark {
    left: 50%;
    top: 62px;
    transform: translateX(-50%);
    color: var(--brand-blue);
    font-size: 52px;
  }
  .back-wordmark .wordmark-mark { background: var(--brand-navy); border-radius: 3px; }
  .contact {
    position: absolute;
    left: 0; right: 0;
    bottom: 22px;
    text-align: center;
    color: var(--paper);
    font-size: 14px;
    line-height: 1.45;
  }
  .contact-name { font-size: 21px; font-weight: 700; margin-bottom: 2px; }
  .contact-role { font-size: 14px; font-weight: 600; }
</style>
</head>
<body>
  <section class="card card-front" aria-label="Business card front">
    <div class="front-backdrop" role="img" aria-label="Decorative background of faint overlapping light-blue squares"></div>
    <div class="wordmark front-wordmark"><span class="wordmark-mark"></span>KORVELTA</div>
    <p class="tagline">Staffing<span class="dot"></span>IT Consulting<span class="dot"></span>Data Services</p>
  </section>

  <section class="card card-back" aria-label="Business card back">
    <div class="back-band"></div>
    <div class="back-frame"></div>
    <div class="wordmark back-wordmark"><span class="wordmark-mark"></span>KORVELTA</div>
    <div class="contact">
      <p class="contact-name">Marcus Hale <span class="contact-role">- President</span></p>
      <p>418 Linden Ave., Harrowgate, IN 47000</p>
      <p>M. 555-014-2290 E. contactus@korveltait.example</p>
      <p>W. www.korveltait.example</p>
    </div>
  </section>
</body>
</html>
```